Accounting Practice Business Card Design

I have a logo I am happy for you to use in the design of the Business Card.
You can edit and change colours as you please, I am not fixated on it.
I am looking for a modern and clean overall feel for the finished design.

The business is a small accounting practice who thrives on word of mouth referrals and this card will be given to all current and prospect clients.

Industry/Entity Type

Accountant

Contact Information for Business Card

Marcus Vell
Level 5, 8 Ashcombe Ridge Road
FERNMOOR RISE VIC 3187
Phone: 9481 3052
Email: mvell@qrnaccountants.com.au
Web: www.qrnaccountants.com.au

Font styles to use
Serif
Sans Serif

Colors
0555a3
3277b5
85acd3
0393ce
33a6d7
85cae6
00a990
33b8a4
9bcb3c

Requirements
Must have
• "The end to your tax problems begin with us"
• "A referral from you is our greatest compliment"
Nice to have
• Modern clean professional

```html
<!DOCTYPE html>
<html lang="en">
<head>
<meta charset="utf-8">
<title>QRN Accountants – Business Card Set</title>
<link href="https://fonts.googleapis.com/css2?family=Barlow:wght@400;500;600;700&display=swap" rel="stylesheet">
<style>
  :root{
    --navy:#0555a3;
    --green:#9bcb3c;
    --teal:#33b8a4;
    --card-light:#ececec;
    --card-paper:#f1f0ef;
    --card-dark:#1c1b1a;
    --ink:#555;
    --ink-soft:#6b6b6b;
    --rule:#9fd3c9;
    --key-face:#f3f3f3;
    --key-edge:#d6d6d6;
    --orange:#e8672a;
    --night:#141414;
    --night-key:#2b2b2b;
  }
  *{box-sizing:border-box;margin:0;padding:0}
  html,body{width:1200px;height:1200px;overflow:hidden;background:#fff}
  body{position:relative;font-family:"Barlow",sans-serif;color:var(--ink)}
  .card{position:absolute;overflow:hidden;box-shadow:0 4px 10px rgba(0,0,0,.22)}
  .card--land{width:448px;height:269px}
  .card--port{width:269px;height:448px}
  .card--light{background:var(--card-light)}
  .card--paper{background:var(--card-paper)}
  .card--dark{background:var(--card-dark)}

  .brand{position:absolute;color:var(--navy);font-weight:700;text-align:center;line-height:.9;letter-spacing:.02em}
  .brand__name{display:block}
  .brand__word{display:block}

  .tagline{position:absolute;left:0;right:0;text-align:center;font-size:10px;line-height:18px;letter-spacing:.01em;text-transform:uppercase}
  .tagline--grey{color:#666}
  .tagline--navy{color:var(--navy)}
  .tagline--dim{color:#1d4f86}

  .band{position:absolute;left:0;top:0;bottom:0;width:41px;background:var(--teal)}
  .holder{position:absolute}
  .holder__name{font-size:19px;font-weight:600;color:var(--ink);letter-spacing:.02em}
  .holder__addr{font-size:11px;color:var(--ink);letter-spacing:.03em;margin-top:1px}
  .contacts{position:absolute;list-style:none}
  .contacts li{height:18.5px;font-size:11px;letter-spacing:.03em;display:flex;align-items:center;border-bottom:1px solid var(--rule);padding-left:8px}
  .contacts li:first-child{border-bottom-color:var(--rule)}
  .icons{position:absolute;width:41px}
  .icons svg{display:block;margin:0 auto 6.5px}

  .calc-display{position:absolute;background:#fff;text-align:right;font-size:15px;color:#c9c9c9;padding:28px 6px 0 0}
  .calc-grid{position:absolute;display:grid;grid-template-columns:repeat(5,1fr);grid-template-rows:repeat(3,1fr);border-left:1px solid #b9e2da;border-top:1px solid #b9e2da}
  .calc-grid span{border-right:1px solid #b9e2da;border-bottom:1px solid #b9e2da;display:flex;align-items:center;justify-content:center;color:#dadada;font-size:15px}

  .keypad{position:absolute;display:grid;grid-template-columns:repeat(4,48px);grid-auto-rows:35px;column-gap:12px;row-gap:10.5px}
  .keypad span{background:var(--key-face);border:2px solid var(--key-edge);border-radius:4px;box-shadow:0 2px 3px rgba(0,0,0,.12);display:flex;align-items:center;justify-content:center;font-size:16px;font-weight:600;color:#777}
  .keypad .key--fn{font-weight:400;color:#aaa}

  .night__name{position:absolute;left:29px;top:30px;font-size:19px;font-weight:500;color:#fff;letter-spacing:.02em}
  .night__role{position:absolute;left:29px;top:53px;font-size:10px;color:var(--orange);font-weight:500}
  .night__list{position:absolute;left:29px;top:106px;list-style:none}
  .night__list li{display:flex;align-items:center;height:16px;font-size:9px;color:#fff;letter-spacing:.02em}
  .night__list i{display:inline-block;width:11px;height:11px;background:var(--orange);border-radius:1px;margin-right:8px}
  .nightpad{position:absolute;left:29px;top:206px;display:grid;grid-template-columns:repeat(4,48px);grid-auto-rows:30px;gap:3px 2.5px}
  .nightpad span{background:var(--night-key);display:flex;align-items:center;justify-content:center;font-size:9px;color:#eee}
  .nightpad .key--wide{grid-column:span 2}
  .nightpad .key--equals{background:var(--orange)}
</style>
</head>
<body>

<!-- Front, landscape -->
<section class="card card--land card--paper" style="left:146px;top:74px">
  <div class="brand" style="left:0;right:0;top:70px">
    <span class="brand__name" style="font-size:62px">QRN</span>
    <span class="brand__word" style="font-size:21px">ACCOUNTANTS</span>
  </div>
  <p class="tagline tagline--grey" style="top:176px">"The end to your tax problems begin with us"<br>"A referral from you is our greatest compliment"</p>
</section>

<!-- Back, landscape with calculator -->
<section class="card card--land card--light" style="left:649px;top:74px">
  <div class="band"></div>
  <svg class="person" style="position:absolute;left:12px;top:48px" width="18" height="20" viewBox="0 0 18 20"><circle cx="9" cy="5.5" r="5" fill="#fff"/><path d="M0 20c0-6 4-8.5 9-8.5s9 2.5 9 8.5z" fill="#fff"/></svg>
  <div class="holder" style="left:49px;top:42px">
    <div class="holder__name">Marcus Vell</div>
    <div class="holder__addr">Level 5, 8 Ashcombe Ridge Road</div>
  </div>
  <div class="icons" style="left:0;top:141px">
    <svg width="10" height="10" viewBox="0 0 10 10"><path d="M2 0l2 2.5-1 1.3a6 6 0 003.2 3.2l1.3-1L10 8 8.5 10A8.5 8.5 0 010 1.5z" fill="#fff"/></svg>
    <svg width="10" height="8" viewBox="0 0 10 8"><rect width="10" height="8" fill="#fff"/><path d="M0 0l5 4 5-4" stroke="#33b8a4" fill="none"/></svg>
    <svg width="11" height="11" viewBox="0 0 11 11"><circle cx="5.5" cy="5.5" r="5" fill="#fff"/><path d="M0.5 5.5h10M5.5 0.5c-3 3-3 7 0 10M5.5 0.5c3 3 3 7 0 10" stroke="#33b8a4" stroke-width=".8" fill="none"/></svg>
    <svg width="9" height="11" viewBox="0 0 9 11"><path d="M4.5 11C1.5 7 0 5.5 0 4.5a4.5 4.5 0 019 0C9 5.5 7.5 7 4.5 11z" fill="#fff"/><circle cx="4.5" cy="4.3" r="1.6" fill="#33b8a4"/></svg>
  </div>
  <ul class="contacts" style="left:41px;top:136px;width:167px">
    <li>9481 3052</li>
    <li>mvell@qrnaccountants.com.au</li>
    <li>www.qrnaccountants.com.au</li>
    <li>Fernmoor Rise Vic 3187</li>
  </ul>
  <div style="position:absolute;left:207px;top:37px;width:241px;height:223px;border:1px solid #b9e2da;border-right:0"></div>
  <div class="brand" style="left:207px;width:241px;top:50px">
    <span class="brand__name" style="font-size:40px">QRN</span>
    <span class="brand__word" style="font-size:13px">ACCOUNTANTS</span>
  </div>
  <div class="calc-display" style="left:211px;top:126px;width:233px;height:50px">0.00</div>
  <div class="calc-grid" style="left:207px;top:176px;width:241px;height:84px">
    <span>1</span><span>2</span><span>3</span><span>4</span><span>+</span>
    <span>5</span><span>6</span><span>7</span><span>8</span><span>-</span>
    <span>9</span><span>0</span><span>*</span><span>/</span><span>=</span>
  </div>
</section>

<!-- Back, portrait with keypad -->
<section class="card card--port card--light" style="left:42px;top:422px">
  <svg style="position:absolute;left:36px;top:37px" width="20" height="21" viewBox="0 0 18 20"><circle cx="9" cy="5.5" r="5" fill="#0555a3"/><path d="M0 20c0-6 4-8.5 9-8.5s9 2.5 9 8.5z" fill="#0555a3"/></svg>
  <div class="holder" style="left:70px;top:32px">
    <div class="holder__name">Marcus Vell</div>
    <div class="holder__addr">Level 5, 8 Ashcombe Ridge Road</div>
  </div>
  <div class="icons" style="left:22px;top:130px;width:24px">
    <svg width="10" height="10" viewBox="0 0 10 10"><path d="M2 0l2 2.5-1 1.3a6 6 0 003.2 3.2l1.3-1L10 8 8.5 10A8.5 8.5 0 010 1.5z" fill="#0555a3"/></svg>
    <svg width="10" height="8" viewBox="0 0 10 8"><rect width="10" height="8" fill="#0555a3"/><path d="M0 0l5 4 5-4" stroke="#ececec" fill="none"/></svg>
    <svg width="11" height="11" viewBox="0 0 11 11"><circle cx="5.5" cy="5.5" r="5" fill="#0555a3"/><path d="M0.5 5.5h10M5.5 0.5c-3 3-3 7 0 10M5.5 0.5c3 3 3 7 0 10" stroke="#ececec" stroke-width=".8" fill="none"/></svg>
    <svg width="9" height="11" viewBox="0 0 9 11"><path d="M4.5 11C1.5 7 0 5.5 0 4.5a4.5 4.5 0 019 0C9 5.5 7.5 7 4.5 11z" fill="#0555a3"/><circle cx="4.5" cy="4.3" r="1.6" fill="#ececec"/></svg>
  </div>
  <ul class="contacts" style="left:62px;top:125px;width:167px">
    <li>9481 3052</li>
    <li>mvell@qrnaccountants.com.au</li>
    <li>www.qrnaccountants.com.au</li>
    <li>Fernmoor Rise Vic 3187</li>
  </ul>
  <div class="keypad" style="left:21px;top:232px">
    <span class="key--fn">mc</span><span class="key--fn">m+</span><span class="key--fn">m-</span><span class="key--fn">mr</span>
    <span>7</span><span>8</span><span>9</span><span class="key--fn">÷</span>
    <span>4</span><span>5</span><span>6</span><span class="key--fn">x</span>
    <span>1</span><span>2</span><span>3</span><span class="key--fn">–</span>
    <span>0</span><span>.</span><span>=</span><span class="key--fn">+</span>
  </div>
</section>

<!-- Front, portrait light -->
<section class="card card--port card--paper" style="left:351px;top:422px">
  <div class="brand" style="left:0;right:0;top:140px">
    <span class="brand__name" style="font-size:62px">QRN</span>
    <span class="brand__word" style="font-size:21px">ACCOUNTANTS</span>
  </div>
  <p class="tagline tagline--navy" style="top:249px;font-size:9px">"The end to your tax problems begin with us"<br>"A referral from you is our greatest compliment"</p>
</section>

<!-- Front, portrait dark -->
<section class="card card--port card--dark" style="left:662px;top:422px">
  <div class="brand" style="left:0;right:0;top:140px">
    <span class="brand__name" style="font-size:62px">QRN</span>
    <span class="brand__word" style="font-size:21px">ACCOUNTANTS</span>
  </div>
  <p class="tagline tagline--dim" style="top:249px;font-size:9px">"The end to your tax problems begin with us"<br>"A referral from you is our greatest compliment"</p>
</section>

<!-- Alternative portrait, night style -->
<section class="card" style="left:944px;top:422px;width:256px;height:426px;background:var(--night);box-shadow:none">
  <svg style="position:absolute;left:0;top:0" width="256" height="426" viewBox="0 0 256 426">
    <polygon points="0,0 56,0 0,56" fill="#e8672a"/>
    <polygon points="256,354 256,426 200,426 230,400" fill="#e8672a"/>
  </svg>
  <div class="night__name">ELLIS BRAND</div>
  <div class="night__role">ACCOUNTANT</div>
  <ul class="night__list">
    <li><i></i>214 HARLOW ST, DUNMERE CA 90412</li>
    <li><i></i>(951)604-2187</li>
    <li><i></i>HELLO@LEDGERLINE.COM</li>
    <li><i></i>WWW.LEDGERLINE.COM</li>
  </ul>
  <div class="nightpad">
    <span>MC</span><span>MR</span><span>MS</span><span>M+</span>
    <span>C</span><span>±</span><span>%</span><span>+</span>
    <span>7</span><span>8</span><span>9</span><span>−</span>
    <span>4</span><span>5</span><span>6</span><span>+</span>
    <span>1</span><span>2</span><span>3</span><span>MC</span>
    <span class="key--wide">0</span><span>.</span><span class="key--equals">=</span>
  </div>
</section>

<!-- Back, landscape simple -->
<section class="card card--land card--light" style="left:42px;top:899px">
  <div class="band"></div>
  <svg style="position:absolute;left:12px;top:48px" width="18" height="20" viewBox="0 0 18 20"><circle cx="9" cy="5.5" r="5" fill="#fff"/><path d="M0 20c0-6 4-8.5 9-8.5s9 2.5 9 8.5z" fill="#fff"/></svg>
  <div class="holder" style="left:49px;top:42px">
    <div class="holder__name">Marcus Vell</div>
    <div class="holder__addr">Level 5, 8 Ashcombe Ridge Road</div>
  </div>
  <div class="brand" style="left:282px;width:124px;top:52px">
    <span class="brand__name" style="font-size:40px">QRN</span>
    <span class="brand__word" style="font-size:13px">ACCOUNTANTS</span>
  </div>
  <div class="icons" style="left:0;top:141px">
    <svg width="10" height="10" viewBox="0 0 10 10"><path d="M2 0l2 2.5-1 1.3a6 6 0 003.2 3.2l1.3-1L10 8 8.5 10A8.5 8.5 0 010 1.5z" fill="#fff"/></svg>
    <svg width="10" height="8" viewBox="0 0 10 8"><rect width="10" height="8" fill="#fff"/><path d="M0 0l5 4 5-4" stroke="#33b8a4" fill="none"/></svg>
    <svg width="11" height="11" viewBox="0 0 11 11"><circle cx="5.5" cy="5.5" r="5" fill="#fff"/><path d="M0.5 5.5h10M5.5 0.5c-3 3-3 7 0 10M5.5 0.5c3 3 3 7 0 10" stroke="#33b8a4" stroke-width=".8" fill="none"/></svg>
    <svg width="9" height="11" viewBox="0 0 9 11"><path d="M4.5 11C1.5 7 0 5.5 0 4.5a4.5 4.5 0 019 0C9 5.5 7.5 7 4.5 11z" fill="#fff"/><circle cx="4.5" cy="4.3" r="1.6" fill="#33b8a4"/></svg>
  </div>
  <ul class="contacts" style="left:41px;top:136px;width:167px">
    <li>9481 3052</li>
    <li>mvell@qrnaccountants.com.au</li>
    <li>www.qrnaccountants.com.au</li>
    <li>Fernmoor Rise Vic 3187</li>
  </ul>
</section>

</body>
</html>
```